Medical group practice

We need a flyer design incorporating the three doctors in the practice, there is a general practitioner, ophthalmologist and an obstetrician & Gynaecologist. see the attached file for the concept. will leave the colour design up to you

Target Market(s)

general public

Industry/Entity Type

Health Care

Colors

Designer to choose colors to be used in the design.

Requirements
Must have
• logos included in attachement

```html
<!DOCTYPE html>
<html lang="en">
<head>
<meta charset="utf-8">
<title>Summit Care Medical – Flyer</title>
<link href="https://fonts.googleapis.com/css2?family=Tinos:ital,wght@0,400;0,700;1,700&family=Arimo:wght@400;700&family=Francois+One&display=swap" rel="stylesheet">
<style>
  :root{
    --red:#e0101c;
    --red-dark:#b50a14;
    --yellow:#ffe400;
    --cyan:#1fb5dc;
    --cyan-dark:#0f8fc0;
    --navy:#1e3f8c;
    --teal:#0c8a8c;
    --purple:#7a1f86;
    --green:#2a9a3e;
    --grey:#8a8a8a;
    --ink:#1c2a56;
    --stage:#9fa2a6;
  }
  *{margin:0;padding:0;box-sizing:border-box}
  html,body{width:1200px;height:710px;overflow:hidden;background:var(--stage)}
  .canvas{position:relative;width:1200px;height:710px}
  .flyer{position:absolute;left:373px;top:15px;width:454px;height:680px;background:#fff;overflow:hidden;
    box-shadow:3px 4px 8px rgba(0,0,0,.35);font-family:"Arimo",Arial,sans-serif}
  .abs{position:absolute}
  .hotline{left:268px;top:0;width:186px;height:40px;background:var(--red);color:var(--yellow);
    font:italic 700 17px/40px "Arimo",Arial,sans-serif;text-align:center}
  .brand{left:44px;top:50px;display:flex;align-items:center;gap:8px}
  .brand-dot{width:20px;height:20px;border-radius:50%;background:var(--red)}
  .brand-name{font:700 28px/1 "Tinos","Times New Roman",serif;color:var(--red);white-space:nowrap}
  .tagline{left:118px;top:84px;font:italic 700 18px/1 "Tinos",serif;color:var(--grey)}
  .address{left:96px;top:108px;font:400 17px/1 "Tinos",serif;color:var(--ink)}
  .swoosh{left:0;top:118px}
  .icon{border-radius:12px}
  .col{text-align:center}
  .doc-name{font-weight:700;font-size:10px;line-height:13px}
  .doc-title{font-size:8.5px;line-height:11px}
  .doc-mail{font-size:8.5px;line-height:12px}
  .services{list-style:none;font-size:12px;line-height:15.8px;margin-top:8px}
  .col-gp{left:0;width:160px;top:282px}
  .col-eye{left:160px;width:160px;top:282px;color:var(--purple)}
  .col-obgyn{left:320px;width:134px;top:258px;color:var(--green)}
  .col-obgyn .doc-name{font-size:9px;line-height:12px}
  .col-gp .doc-name,.col-gp .doc-title,.col-gp .doc-mail,.col-gp .services{color:var(--cyan-dark)}
  .col-eye .doc-title,.col-eye .doc-mail{color:var(--purple)}
  .col-obgyn .doc-name,.col-obgyn .doc-title,.col-obgyn .doc-mail{color:var(--teal)}
  .divider{width:1px;background:#777;top:200px;height:270px}
  .hours-band{left:0;top:456px}
  .hours-label{left:24px;top:500px;font:400 20px/20px "Francois One",Impact,sans-serif;color:var(--yellow);
    transform:rotate(15deg);transform-origin:left top;text-align:center;white-space:nowrap}
  .hours{left:104px;top:520px;width:180px;font:700 15px/20px "Arimo",Arial,sans-serif;color:#fff;
    text-align:right;white-space:nowrap}
  .footer{left:0;top:567px;width:454px;height:113px;background:linear-gradient(180deg,var(--red) 0%,var(--red-dark) 100%)}
  .footer-line{position:absolute;left:18px;color:#fff;font-size:11px;white-space:nowrap}
  .footer-line b{color:var(--yellow);font-size:15px;font-weight:700}
</style>
</head>
<body>
<div class="canvas">
  <article class="flyer">
    <div class="abs hotline">(555) 210 3040/3041</div>

    <header>
      <div class="abs brand"><span class="brand-dot"></span><span class="brand-name">SUMMIT CARE Medical</span></div>
      <div class="abs tagline">your health is our priority</div>
      <div class="abs address">42 Harbour Road, Port Alder, Westvale</div>
      <svg class="abs swoosh" width="454" height="50" viewBox="0 0 454 50">
        <path d="M16 20 Q230 52 440 18 Q240 40 16 20Z" fill="#c9c9c9"/>
        <path d="M16 20 Q230 60 440 18 Q236 48 16 20Z" fill="var(--red)"/>
      </svg>
    </header>

    <div class="abs icon" style="left:36px;top:168px;width:78px;height:82px;background:linear-gradient(135deg,#2ab0d8,#0f6fa8)" role="img" aria-label="General practice emblem: medical cross with family and stethoscope"></div>
    <div class="abs icon" style="left:196px;top:192px;width:94px;height:44px;border-radius:50%;background:linear-gradient(90deg,#7a1f86,#3a9ad0)" role="img" aria-label="Ophthalmology emblem: eye with globe"></div>
    <div class="abs icon" style="left:352px;top:168px;width:82px;height:70px;border-radius:40px;background:linear-gradient(135deg,#1e3f8c,#2a9a3e)" role="img" aria-label="Obstetrics emblem: mother and child shapes"></div>

    <div class="abs divider" style="left:160px"></div>
    <div class="abs divider" style="left:320px"></div>

    <section class="abs col col-gp">
      <div class="doc-name">Dr Kevin Marsh, MD</div>
      <div class="doc-title">General Practitioner</div>
      <div class="doc-mail">k.marsh.doc@mailbox.com</div>
      <ul class="services">
        <li>General Checks</li><li>Annual Check ups</li><li>Wound Care/ Dressings</li><li>Incision &amp; Drainage</li>
        <li>Suturing Lacerations</li><li>Pain Injections</li><li>Glucose Checks</li><li>Foreign Body Removal</li>
      </ul>
    </section>

    <section class="abs col col-eye">
      <div class="doc-name">Dr Lucia R Vance, MD</div>
      <div class="doc-title">Surgeon Ophthamologist</div>
      <div class="doc-mail">l.vance.eye@mailbox.com</div>
      <ul class="services">
        <li>Eye Disease Examination</li><li>Surgery of Pterygium</li><li>Cataract</li><li>Glaucoma</li>
        <li>EMERGENCY :</li><li>Conjuctivitis</li><li>Traumatism</li><li>Foreign Body</li><li>&amp;</li><li>More</li>
      </ul>
    </section>

    <section class="abs col col-obgyn">
      <div class="doc-name">Dr Anil Desai<br>BMedSci, MBBS, DM(O &amp; G)<br>FACOG</div>
      <div class="doc-title">Obstetrician &amp; Gynaecologist</div>
      <div class="doc-mail">a.desai.doc@mailbox.com</div>
      <ul class="services">
        <li>OBSTETERICS :</li><li>Prenatal Care</li><li>Delivery</li><li>Postnatal Checks</li><li>High Risk Pregnancy</li>
        <li>GYNAECOLOGY :</li><li>Pap Smears</li><li>Abnormal-</li><li>-Vaginal Bleeding</li><li>Fibroids</li>
        <li>Colposcopy</li><li>Family Planning</li><li>Infertility</li><li>Cancer Screening</li><li>&amp; more</li>
      </ul>
    </section>

    <svg class="abs hours-band" width="454" height="112" viewBox="0 0 454 112">
      <path d="M0 16 Q110 -4 220 24 Q290 42 320 40 L320 112 L0 112Z" fill="var(--red)"/>
      <path d="M0 27 Q110 8 220 35 Q290 52 320 50 L320 112 L0 112Z" fill="#fff"/>
      <path d="M0 33 Q110 15 220 41 Q290 58 320 56 L320 112 L0 112Z" fill="var(--cyan)"/>
    </svg>
    <div class="abs hours-label">opening<br>hours</div>
    <div class="abs hours">mon-fri : 9 am - 6 pm<br>saturdays : 10 am - 5 pm</div>

    <footer class="abs footer">
      <div class="footer-line" style="top:26px">General Practitioner <b>(555) 301 4471</b> &nbsp;Ophthamologist <b>(555) 302 6180</b></div>
      <div class="footer-line" style="top:64px">Obstetrician/Gynaecologist <b>(555) 303 2290, (555) 304 7715</b></div>
    </footer>
  </article>
</div>
</body>
</html>
```